Velborne Systems needs a business card

The logo we have uploaded is going to be the image centered on the back.
The business card color is going to be black. Increase the contrast in the logo and lettering so the grey stands out from the black and is more readable. Keep the shadow effect if you can.
On the front, the only part of the logo that should be used is the Egyptian character. We would like the following information included: Name (first last), Title, Phone number, email and company name (Velborne Systems).
The images of colored sound waves we uploaded is a concept we would like implemented on the front as well but please do not use the exact image. It is for guideline purposes.
Get creative with the empty space. We are a technology company that deals with sound and lights. Please not too busy.
Thank you, we look forward to all your submissions.

```html
<!DOCTYPE html>
<html lang="en">
<head>
<meta charset="utf-8">
<title>Velborne Systems – Business Card</title>
<link rel="stylesheet" href="https://fonts.googleapis.com/css2?family=Open+Sans:wght@400;600;700&display=swap">
<style>
  :root {
    --bg: #8d8d8d;
    --card-black: #030303;
    --brand-red: #ec1c24;
    --rule-white: #f4f4f4;
    --logo-grey: #8e979c;
    --text-white: #ffffff;
  }
  * { margin: 0; padding: 0; box-sizing: border-box; }
  html, body {
    width: 1200px;
    height: 900px;
    overflow: hidden;
    background: var(--bg);
    font-family: "Open Sans", Arial, sans-serif;
  }
  .canvas {
    position: relative;
    width: 1200px;
    height: 900px;
  }
  .card {
    position: absolute;
    width: 580px;
    height: 330px;
    background: var(--card-black);
    overflow: hidden;
    box-shadow: 0 10px 24px rgba(0,0,0,.35);
  }

  /* Back of card */
  .card-back { left: 540px; top: 80px; }
  .card-back .wordmark {
    position: absolute;
    left: 0; right: 0; top: 100px;
    display: flex; justify-content: center; align-items: center; gap: 14px;
  }
  .card-back .rule-white {
    position: absolute; left: 0; right: 0; top: 238px; height: 7px;
    background: var(--rule-white);
  }
  .card-back .band-red {
    position: absolute; left: 0; right: 0; top: 251px; height: 44px;
    background: var(--brand-red);
  }

  /* Logo stand-in */
  .brand-square {
    width: 26px; height: 26px;
    background: var(--brand-red);
    flex: none;
  }
  .brand-name {
    font-weight: 700;
    font-size: 34px;
    letter-spacing: 1px;
    text-transform: uppercase;
    color: var(--logo-grey);
    white-space: nowrap;
  }

  /* Front of card */
  .card-front { left: 80px; top: 460px; }
  .card-front .wordmark {
    position: absolute; left: 36px; top: 56px;
    display: flex; align-items: center; gap: 10px;
  }
  .card-front .brand-name { font-size: 24px; }
  .card-front .brand-square { width: 18px; height: 18px; }

  .person {
    position: absolute; right: 34px; top: 92px;
    text-align: right;
  }
  .person-name {
    color: var(--brand-red);
    font-weight: 600;
    font-size: 19px;
    letter-spacing: .5px;
    text-transform: uppercase;
  }
  .person-title {
    color: var(--text-white);
    font-size: 15px;
    margin-top: 1px;
  }

  .band-contact {
    position: absolute; left: 0; right: 0; top: 168px; height: 110px;
    background: var(--brand-red);
    display: flex; justify-content: space-between;
    padding: 22px 34px 0 26px;
  }
  .rule-contact {
    position: absolute; left: 0; right: 0; top: 282px; height: 6px;
    background: var(--rule-white);
  }
  .contact-group {
    color: var(--text-white);
    font-size: 14px;
    line-height: 1.6;
  }
  .contact-group.phones { padding-top: 22px; }
  .contact-group.online { padding-top: 34px; }
  .contact-line {
    display: flex; align-items: center; gap: 6px;
    white-space: nowrap;
  }
  .contact-line.indent { padding-left: 0; }
  .icon { width: 12px; height: 12px; flex: none; fill: var(--text-white); }
</style>
</head>
<body>
<main class="canvas">

  <section class="card card-back" aria-label="Business card back">
    <div class="wordmark">
      <span class="brand-square"></span>
      <span class="brand-name">Velborne Systems</span>
    </div>
    <div class="rule-white"></div>
    <div class="band-red"></div>
  </section>

  <section class="card card-front" aria-label="Business card front">
    <div class="wordmark">
      <span class="brand-square"></span>
      <span class="brand-name">Velborne Systems</span>
    </div>

    <div class="person">
      <p class="person-name">Adrian Kessler</p>
      <p class="person-title">Managing Director</p>
    </div>

    <div class="band-contact">
      <div class="contact-group address">
        <p class="contact-line">
          <svg class="icon" viewBox="0 0 12 12"><path d="M6 0a4 4 0 0 0-4 4c0 3 4 8 4 8s4-5 4-8a4 4 0 0 0-4-4zm0 5.6A1.6 1.6 0 1 1 6 2.4a1.6 1.6 0 0 1 0 3.2z"/></svg>
          1234, Address Goes Here,
        </p>
        <p class="contact-line">Country Name, 123456</p>
      </div>

      <div class="contact-group phones">
        <p class="contact-line">
          <svg class="icon" viewBox="0 0 12 12"><path d="M1 3c1-2 9-2 10 0v1.5H8.5V3.5h-5v1H1zM2.5 6h7l1 5h-9z"/></svg>
          123.456.7890
        </p>
        <p class="contact-line">
          <svg class="icon" viewBox="0 0 12 12"><path d="M3 1h5l2 2v8H3zM1 4h1.5v7H1z"/></svg>
          123.456.7890
        </p>
      </div>

      <div class="contact-group online">
        <p class="contact-line">
          <svg class="icon" viewBox="0 0 12 12"><path d="M0 2.5h12v7H0zm1 1v.4l5 3 5-3v-.4z"/></svg>
          info@youremail.com
        </p>
        <p class="contact-line">
          <svg class="icon" viewBox="0 0 12 12"><path d="M5 7 7 5M4.5 5.5 2.8 7.2a1.6 1.6 0 0 0 2.2 2.2L6.5 7.8M7.5 6.5l1.7-1.7A1.6 1.6 0 0 0 7 2.6L5.5 4.2" fill="none" stroke="#fff" stroke-width="1.3" stroke-linecap="round"/></svg>
          www.website.com
        </p>
      </div>
    </div>
    <div class="rule-contact"></div>
  </section>

</main>
</body>
</html>
```